Redesign of existing business card

I would like the "signage" attachment converted into a business card. This needs to be double sided aswell, keeping the phone number and names on the front, and the email + website on the back.

Second attachment is the current business card design.

Larger font for contact details is required.

Must keep to original color themes (electric blue, silver/grey etc)

Back of the card to have blue background with white writing.

Industry/Entity Type

Business

Contact Information for Business Card

Refer to existing design from attachments

Requirements
Must have
• Refer to existing design from attachments
Nice to have

```html
<!DOCTYPE html>
<html lang="en">
<head>
<meta charset="utf-8">
<title>Voltaro Electrical Services – Business Card</title>
<link rel="stylesheet" href="https://fonts.googleapis.com/css2?family=Open+Sans:wght@700;800&display=swap">
<style>
  :root {
    --backdrop: #1c1c1e;
    --electric-blue: #3a55ad;
    --electric-blue-deep: #2e4597;
    --electric-blue-light: #4865bf;
    --card-white: #ffffff;
    --silver: #8a8f99;
    --type-white: #ffffff;
  }
  * { box-sizing: border-box; margin: 0; padding: 0; }
  html, body {
    width: 1200px;
    height: 1000px;
    overflow: hidden;
    background: var(--backdrop);
    font-family: "Open Sans", Arial, sans-serif;
  }
  .canvas {
    position: relative;
    width: 1200px;
    height: 1000px;
  }
  .card {
    position: absolute;
    width: 620px;
    height: 354px;
    border-radius: 28px;
    overflow: hidden;
    background: linear-gradient(135deg, var(--electric-blue-light), var(--electric-blue) 55%, var(--electric-blue-deep));
    box-shadow: 0 18px 40px rgba(0,0,0,0.55);
  }

  /* Back of card */
  .card--back { left: 110px; top: 90px; }
  .card--back .brand-mark {
    position: absolute;
    left: 44px; top: 52px;
    width: 250px; height: 250px;
    border: 26px solid var(--type-white);
    border-radius: 50%;
  }
  .card--back .brand-name {
    position: absolute;
    left: 320px; top: 80px;
    color: var(--type-white);
    font-weight: 800;
    line-height: 1;
  }
  .brand-name .brand-word { display: block; font-size: 54px; letter-spacing: 2px; }
  .brand-name .brand-sub { display: block; font-size: 17px; letter-spacing: 1.5px; margin-top: 6px; }
  .card--back .contact-list {
    position: absolute;
    right: 34px; top: 222px;
    list-style: none;
    text-align: right;
    color: var(--type-white);
    font-weight: 800;
    font-size: 19px;
    line-height: 1.55;
  }

  /* Front of card */
  .card--front { left: 470px; top: 530px; }
  .card--front .white-field {
    position: absolute; inset: 0;
    width: 100%; height: 100%;
  }
  .card--front .brand-mark {
    position: absolute;
    left: 40px; top: 70px;
    width: 130px; height: 130px;
    border: 14px solid var(--silver);
    border-radius: 50%;
  }
  .card--front .brand-name {
    position: absolute;
    left: 190px; top: 88px;
    color: var(--silver);
    font-weight: 800;
    line-height: 1;
  }
  .card--front .brand-name .brand-word { font-size: 62px; }
  .card--front .brand-name .brand-sub { font-size: 20px; }
  .card--front .phone {
    position: absolute;
    left: 220px; top: 250px;
    display: flex;
    align-items: center;
    gap: 16px;
    color: var(--type-white);
    font-weight: 800;
    font-size: 44px;
    letter-spacing: 1px;
  }
  .phone-icon { width: 38px; height: 38px; }
</style>
</head>
<body>
<main class="canvas">

  <section class="card card--back" aria-label="Business card back">
    <span class="brand-mark" aria-hidden="true"></span>
    <h1 class="brand-name">
      <span class="brand-word">VOLTARO</span>
      <span class="brand-sub">ELECTRICAL SERVICES</span>
    </h1>
    <ul class="contact-list">
      <li>www.voltaroelectrical.com.au</li>
      <li>hello@voltaroelectrical.com.au</li>
    </ul>
  </section>

  <section class="card card--front" aria-label="Business card front">
    <svg class="white-field" viewBox="0 0 620 354" preserveAspectRatio="none" aria-hidden="true">
      <polygon points="0,0 600,0 0,250" fill="var(--card-white)"/>
    </svg>
    <span class="brand-mark" aria-hidden="true"></span>
    <h2 class="brand-name">
      <span class="brand-word">VOLTARO</span>
      <span class="brand-sub">ELECTRICAL SERVICES</span>
    </h2>
    <p class="phone">
      <svg class="phone-icon" viewBox="0 0 24 24" aria-hidden="true">
        <path fill="var(--type-white)" d="M6.6 10.8a15.1 15.1 0 0 0 6.6 6.6l2.2-2.2a1 1 0 0 1 1-.25 11.4 11.4 0 0 0 3.6.57 1 1 0 0 1 1 1V20a1 1 0 0 1-1 1A17 17 0 0 1 3 4a1 1 0 0 1 1-1h3.5a1 1 0 0 1 1 1c0 1.25.2 2.45.57 3.57a1 1 0 0 1-.25 1z"/>
      </svg>
      <span>0400 318 547</span>
    </p>
  </section>

</main>
</body>
</html>
```